Retail Jewelry Business Card Design Project

We are in need of a new business card design for a retail jewelry store. This store is in the business of fine jewelry including but not specific to bridal jewelry, diamonds, designer jewelry and watches.

This store has been in business for 20 years but continues to strive for a modern professional appeal. The main colors use for this business are a royal blue, white and silver.

Target Market(s)

Target market is ages 18-50

Industry/Entity Type

Jewelry

Requirements
Must have
• Sales Person Name
Sales Person Email Address

Store Address
Store Phone
Website

Standard business card size. No odd shapes or sizes.
Nice to have
• Overall modern feel for card.

We have thought that a design with a nice feature of the logo on the back of the card would be nice but open to ideas.
Should not have
• No specific images of jewelry should be used.

```html
<!DOCTYPE html>
<html lang="en">
<head>
<meta charset="utf-8">
<title>Marlow Vance Fine Jewelry – Business Card</title>
<link rel="stylesheet" href="https://fonts.googleapis.com/css2?family=Roboto:wght@300;400;700&display=swap">
<style>
  :root {
    --backdrop: #2b2d30;
    --royal-blue: #25307a;
    --royal-blue-deep: #1d2666;
    --silver: #e4e6ee;
    --white: #ffffff;
  }
  * { margin: 0; padding: 0; box-sizing: border-box; }
  html, body {
    width: 1200px;
    height: 900px;
    overflow: hidden;
    background: var(--backdrop);
  }
  .canvas {
    position: relative;
    width: 1200px;
    height: 900px;
    font-family: "Roboto", Arial, sans-serif;
  }
  .card {
    position: absolute;
    left: 320px;
    width: 560px;
    height: 320px;
    background: linear-gradient(160deg, var(--royal-blue) 0%, var(--royal-blue-deep) 100%);
    box-shadow: 0 12px 30px rgba(0, 0, 0, 0.45);
    color: var(--silver);
  }
  .card--front { top: 110px; }
  .card--back  { top: 470px; }

  .brand {
    font-weight: 400;
    color: var(--silver);
    line-height: 1.1;
  }
  .card--front .brand {
    position: absolute;
    left: 0;
    right: 0;
    top: 120px;
    text-align: center;
    font-size: 40px;
    letter-spacing: 1px;
  }
  .card--back .brand {
    position: absolute;
    left: 36px;
    top: 30px;
    font-size: 22px;
    letter-spacing: 0.5px;
  }

  .contact-person {
    position: absolute;
    left: 170px;
    top: 132px;
  }
  .contact-person__name {
    font-weight: 700;
    font-size: 17px;
    letter-spacing: 1.5px;
    color: var(--white);
  }
  .contact-person__email {
    margin-top: 4px;
    font-weight: 300;
    font-size: 13px;
    letter-spacing: 2.5px;
  }

  .store-details {
    position: absolute;
    right: 36px;
    bottom: 32px;
    text-align: right;
    font-weight: 300;
    font-size: 13px;
    letter-spacing: 2.5px;
    line-height: 1.5;
  }
  .store-details__phone { margin-left: 28px; }
</style>
</head>
<body>
<main class="canvas">
  <section class="card card--front" aria-label="Card front">
    <h1 class="brand">Marlow Vance Fine Jewelry</h1>
  </section>

  <section class="card card--back" aria-label="Card back">
    <p class="brand">Marlow Vance Fine Jewelry</p>

    <div class="contact-person">
      <p class="contact-person__name">Marlow Vance Ellery</p>
      <p class="contact-person__email">marlow@marlowvancejewelry.com</p>
    </div>

    <div class="store-details">
      <p><span class="store-details__web">www.marlowvancejewelry.com</span><span class="store-details__phone">(555) 214 0386</span></p>
      <p class="store-details__address">418 Calder Avenue Bayport, FL 32999</p>
    </div>
  </section>
</main>
</body>
</html>
```